Website design improvement for existing site

We would like design ideas for how the inner pages (not the homepage) of www.quillbrookmedia.com could be improved. We don't want to totally redesign the website. We want to improve / enhance / develop it further to look high-end, sophisticated and visually stunning.

Target Market(s)

High end video production clients. National and international TV networks and brands wanting commercial filming.

Industry/Entity Type

Videography

Other font styles liked:
• Existing site fonts

Requirements
Must have
• Improvement on the existing inner pages without totally re-working the design. We want to achieve a high-end sophisticated look with the existing branding (colours, images etc)
Nice to have
• Any ideas for improving the homepage are also welcome but we are mostly happy with this page so it is not the priority.
Should not have
• Any major changes to colours, styles etc.

```html
<!DOCTYPE html>
<html lang="en">
<head>
<meta charset="utf-8">
<title>About — Quillbrook Media</title>
<link rel="stylesheet" href="https://fonts.googleapis.com/css2?family=Oswald:wght@500&family=Montserrat:wght@400;500&family=Space+Mono&display=swap">
<style>
:root{
  --black:#000;
  --ink:#222;
  --red:#d8161b;
  --paper:#ededed;
  --white:#fff;
  --grey-text:#bbb;
}
*{margin:0;padding:0;box-sizing:border-box}
html,body{width:1200px;height:3644px;overflow:hidden}
body{position:relative;background:var(--white);font-family:"Space Mono",monospace;color:var(--ink)}
.abs{position:absolute}
.site-nav{left:0;top:0;width:1200px;height:58px;background:var(--black)}
.brand{left:26px;top:10px;display:flex;align-items:center;gap:10px;color:var(--white);font-family:"Oswald",sans-serif;font-size:22px;letter-spacing:1px}
.brand-dot{width:30px;height:30px;border-radius:50%;background:var(--red)}
.nav-link{top:22px;font-family:"Montserrat",sans-serif;font-size:13px;letter-spacing:4px;color:var(--grey-text)}
.nav-link.active{color:var(--red)}
.nav-link.cta{color:var(--white)}
.hero{left:0;top:58px;width:1200px;height:802px;background:radial-gradient(ellipse at 60% 30%,#6a5444 0%,#3e3129 45%,#221b17 100%)}
.hero-tag{left:0;top:360px;width:1200px;text-align:center;color:var(--white);font-family:"Montserrat",sans-serif;font-size:20px;letter-spacing:3px;line-height:36px}
.hero-button{left:370px;top:472px;width:460px;height:114px;border:5px solid var(--white);background:rgba(40,32,28,.85);color:var(--white);font-family:"Oswald",sans-serif;font-size:46px;display:flex;align-items:center;justify-content:center}
.about{left:0;top:860px;width:1200px;height:1790px;background:var(--paper)}
.photo{background:linear-gradient(160deg,#8c8a85,#3a3835)}
.founder-photo{left:0;top:975px;width:435px;height:830px;background:linear-gradient(170deg,#b8b4ab 0%,#5a534c 50%,#1d1c1c 100%)}
.assistant-photo{left:768px;top:1828px;width:432px;height:722px;background:linear-gradient(190deg,#c9c4bb 0%,#6b5a4c 55%,#232120 100%)}
.member-name{font-family:"Oswald",sans-serif;font-size:38px;color:var(--ink)}
.member-role{font-family:"Montserrat",sans-serif;font-size:24px;color:var(--red)}
.rule{height:2px;background:var(--red)}
.bio p{font-size:13px;line-height:24px;margin-bottom:16px;letter-spacing:.2px}
.band-photo{left:0;top:2650px;width:1200px;height:318px;background:linear-gradient(90deg,#4a3a30,#b9b4ae 45%,#6e665e 75%,#2c2622)}
.collab{left:450px;top:3020px;width:560px;font-size:13px;line-height:24px}
.partners{left:195px;top:3210px;width:815px;height:80px;display:flex;align-items:center;justify-content:space-between;font-family:"Montserrat",sans-serif;font-weight:500;font-size:26px;color:var(--ink)}
.partner{display:flex;align-items:center;gap:8px}
.partner-sq{width:28px;height:28px;background:var(--red)}
.footer{left:0;top:3420px;width:1200px;height:224px;background:var(--black);color:var(--white);text-align:center}
.social{display:flex;justify-content:center;gap:30px;margin-top:40px;font-family:"Montserrat",sans-serif;font-size:15px;letter-spacing:1px}
.legal{margin-top:30px;font-family:"Montserrat",sans-serif;font-size:12px;line-height:19px}
</style>
</head>
<body>
<header class="abs site-nav">
  <div class="abs brand"><span class="brand-dot"></span>QUILLBROOK MEDIA</div>
  <span class="abs nav-link" style="left:495px">HOME</span>
  <span class="abs nav-link active" style="left:600px">ABOUT</span>
  <span class="abs nav-link" style="left:715px">PROCESS</span>
  <span class="abs nav-link" style="left:858px">BRAND STORIES</span>
  <span class="abs nav-link cta" style="left:1078px">CONTACT</span>
</header>

<section class="abs hero" role="img" aria-label="Close-up film still of a chef at work behind a wooden shutter"></section>
<div class="abs hero-tag">EXPERT CINEMATOGRAPHY.<br>BEAUTIFUL STORYTELLING.</div>
<div class="abs hero-button">Who Are We?</div>

<section class="abs about"></section>

<div class="abs founder-photo" role="img" aria-label="Founder smiling while holding a cinema camera in a kitchen"></div>
<div class="abs rule" style="left:435px;top:1242px;width:765px"></div>
<h2 class="abs member-name" style="left:535px;top:1155px">Rowan Quillbrook</h2>
<div class="abs member-role" style="left:535px;top:1205px">The Founder</div>
<div class="abs bio" style="left:533px;top:1262px;width:470px">
  <p>Quillbrook Media was set up by Rowan Quillbrook. The idea? To help businesses harness the narrative power of film to tell better brand stories. To allow companies to use a creative, visual medium to produce unique and beautiful narratives. Brand messages that truly engage with customers and better define who they are.</p>
  <p>Living in Hull and working around the UK, Rowan's a commercial filmmaker, camera operator, and director of photography. He's worked with all the major UK terrestrial's - Northwave, Vale TV, Lumen &amp; Brightcast. His experience includes making brand stories, advertisements, corporate films, training videos and documentary films. He is also a AAB-approved Aerial Cinematographer and holder of a Permission for Commercial Operations for drone filming &amp; photography.</p>
</div>

<div class="abs assistant-photo" role="img" aria-label="Production assistant operating a camera on a tripod"></div>
<div class="abs rule" style="left:0;top:2005px;width:768px"></div>
<h2 class="abs member-name" style="left:210px;top:1955px">Tessa Marlow</h2>
<div class="abs member-role" style="left:210px;top:2008px">Production Assistant</div>
<div class="abs bio" style="left:210px;top:2062px;width:450px">
  <p>Tessa is our production assistant and b-cam operator also based in Hull. Having completed her BA (Hons) Media Production degree at the University of Ashford in 2016, Tessa has 5 years experience in photography and film.</p>
  <p>Her drive and dedication to making every shot the best it can be, and her enthusiasm for the art brings our productions to a whole new level.</p>
</div>

<div class="abs band-photo" role="img" aria-label="Camera monitor showing a shot during a kitchen shoot"></div>
<p class="abs collab">Rowan  collaborates with a team of skilled pre-production, production &amp; post-production specialists from Leeds and York to London. He's worked with some of the UK's biggest creative agencies and helped tell the brand stories of companies of all sizes and sectors, working with both agencies and businesses.</p>

<div class="abs partners">
  <span class="partner"><span class="partner-sq"></span>Northwave</span>
  <span class="partner">Harrowfield</span>
  <span class="partner">Brightcast</span>
  <span class="partner">Kestrel</span>
  <span class="partner">Elmstone</span>
  <span class="partner">Vale TV</span>
</div>

<footer class="abs footer">
  <div class="social"><span>Linkwise</span><span>Photoloop</span></div>
  <div class="legal">Quillbrook Media Ltd<br>01632 960412 | hello@quillbrookmedia.com<br>Company No. 12345678<br>VAT No. 987654321</div>
</footer>
</body>
</html>
```